International Water Charity needs brochure

We need a brochure design to attract new donors and work teams to our project. Our primary focus is water wells and health projects. This brochure should tell what we do, how we do it (install water systems) and then have a small portion advertising the need for work teams.

Please see our website for more information www.lumarendserves.org

Some of our marketing materials are here.
https://files.brindlecove.net/share?id=Kx93PqLmZt7RwVb2NcYd5HsJ8fGa&mode=view

Please pull the text from our current website.....brochure size could 8.5 x 11 bifold or trifold.

Please have a section promoting teams and then a section showing information from our about page.  Will we use this brochure at conferences and to send to donors to supply general information. 

Thank you!!

```html
<!DOCTYPE html>
<html lang="en">
<head>
<meta charset="utf-8">
<title>Lumarend Serves – Brochure Spread</title>
<link href="https://fonts.googleapis.com/css2?family=Exo+2:wght@400;500;600&family=PT+Sans:wght@400;700&display=swap" rel="stylesheet">
<style>
:root{
  --bg:#dcdbd7;
  --paper:#ffffff;
  --gold:#c9ab64;
  --blue:#2f5d9f;
  --ink:#5a5a5a;
  --soft:#8a8a8a;
  --orange:#e5a23a;
  --green:#6aa84f;
  --sky:#5b8fd1;
  --red:#c0392b;
}
*{margin:0;padding:0;box-sizing:border-box}
html,body{width:1200px;height:804px;overflow:hidden;background:var(--bg)}
body{position:relative;font-family:"PT Sans",sans-serif;color:var(--ink)}
.page{position:absolute;top:77px;width:500px;height:650px;background:var(--paper);overflow:hidden}
.page--left{left:100px;box-shadow:-2px 3px 10px rgba(0,0,0,.12)}
.page--right{left:600px;box-shadow:2px 3px 10px rgba(0,0,0,.12);background:linear-gradient(90deg,#eeeeee 0,#fff 18px)}
.abs{position:absolute}
.heading{font-family:"Exo 2",sans-serif;font-weight:400;line-height:1}
.heading .gold{color:var(--gold)}
.heading .blue{color:var(--blue)}
.hero{left:0;top:0}
.who{left:30px;top:318px;font-size:38px}
.who-sub{left:176px;top:358px;font-family:"Exo 2",sans-serif;font-size:8px;letter-spacing:1px;color:var(--blue);font-weight:600}
.dotted{border-top:1px dotted #9aa9c0}
.team-photo-small{left:30px;top:395px}
.mission{left:30px;top:548px;width:240px;font-size:9.5px;line-height:1.55}
.about{left:272px;top:300px;width:200px;font-size:9.5px;line-height:1.55}
.stats{left:272px;top:400px;width:200px;list-style:none}
.stats li{font-family:"Exo 2",sans-serif;font-size:15px;color:#555;padding:12px 0 10px;border-bottom:1px dotted #b7b7b7;white-space:nowrap}
.stats li:last-child{border-bottom:none}
.stats b{font-weight:500;color:var(--blue);margin-left:6px}
.folio{font-size:8.5px;color:#7c92b8;display:flex;align-items:center;gap:8px}
.folio .num{width:10px;height:10px;background:#b9c6db;color:#fff;font-size:7px;display:flex;align-items:center;justify-content:center}
.folio--left{left:30px;top:620px}
.folio--right{right:24px;top:612px}
.history{left:160px;top:22px;font-size:32px}
.rule{height:0;border-top:1px dotted #b9b9b9}
.tl-year{position:absolute;font-family:"Exo 2",sans-serif;font-size:7px;letter-spacing:1px;color:#555;font-weight:600}
.tl-bar{position:absolute;height:3px;width:50px}
.tl-box{position:absolute;width:52px;border:1px solid;border-radius:7px;padding:5px 4px;font-size:6.3px;line-height:1.45;text-align:justify;background:#fff;color:#666}
.our-team{left:140px;top:258px;font-size:32px}
.member{position:absolute;left:46px;width:310px}
.member h3{font-family:"Exo 2",sans-serif;font-size:8px;font-weight:600;letter-spacing:.6px;color:var(--blue);margin-bottom:6px;position:relative}
.member h3 svg{position:absolute;left:-20px;top:4px}
.member p{font-size:7.6px;line-height:1.55;color:#6a6a6a}
.member-sep{position:absolute;left:46px;width:290px;border-top:1px dotted #b9b9b9}
.portrait{position:absolute;left:364px;width:82px;height:76px;border:2px solid var(--gold);border-radius:12px;overflow:hidden}
.portrait span{display:block;width:100%;height:100%}
</style>
</head>
<body>

<section class="page page--left">
  <svg class="abs hero" width="500" height="320" viewBox="0 0 500 320" role="img" aria-label="Photo of three volunteers standing beside a freshly drilled well spouting water, tropical foliage behind">
    <defs>
      <linearGradient id="heroFill" x1="0" y1="0" x2="0" y2="1">
        <stop offset="0" stop-color="#3f5a2e"/>
        <stop offset=".55" stop-color="#6b6a4c"/>
        <stop offset="1" stop-color="#8a7a62"/>
      </linearGradient>
    </defs>
    <path d="M0 0H500V165Q300 282 0 282Z" fill="url(#heroFill)"/>
    <path d="M0 282Q300 282 500 165L500 182Q300 300 0 300Z" fill="var(--gold)"/>
  </svg>

  <h2 class="abs heading who"><span class="gold">Who</span> <span class="blue">We Are</span></h2>
  <div class="abs who-sub">ABOUT US</div>
  <div class="abs dotted" style="left:30px;top:376px;width:220px"></div>
  <div class="abs dotted" style="left:30px;top:380px;width:220px"></div>

  <svg class="abs team-photo-small" width="220" height="130" viewBox="0 0 220 130" role="img" aria-label="Photo of a young boy and a smiling woman in a village home">
    <defs>
      <linearGradient id="smallFill" x1="0" y1="0" x2="1" y2="0">
        <stop offset="0" stop-color="#4b3a2e"/>
        <stop offset=".6" stop-color="#7a4a3a"/>
        <stop offset="1" stop-color="#5a4538"/>
      </linearGradient>
    </defs>
    <path d="M0 0H220V70Q150 112 0 112Z" fill="url(#smallFill)"/>
    <path d="M0 112Q150 112 220 70L220 80Q150 124 0 124Z" fill="var(--blue)"/>
  </svg>

  <p class="abs mission">Mission Statement: Improving the lives of Central Americans through the development of clean water systems and healthy living conditions. Lumarend Serves was born out of the First Harbor Chapel</p>

  <p class="abs about">of Cedar Point, a church that has a real and lasting commitment to missions. Through the support of church staff and Senior Pastor Dr. Alan Whitcombe, the project has continued to grow in its impact. Our current focus area is in Las Brisas, Costa Rica.</p>

  <ul class="abs stats">
    <li>LIVES TOUCHED: <b>3200</b></li>
    <li>WELLS DRILLED: <b>29</b></li>
    <li>FUNDS RAISED: <b>$200k</b></li>
  </ul>

  <div class="abs folio folio--left"><span class="num">2</span>www.lumarendserves.org</div>
</section>

<section class="page page--right">
  <h2 class="abs heading history"><span class="gold">His</span><span class="blue">tory</span></h2>
  <div class="abs rule" style="left:178px;top:62px;width:80px"></div>
  <div class="abs rule" style="left:178px;top:66px;width:80px"></div>

  <div class="tl-year" style="left:42px;top:126px">IN 2014</div>
  <div class="tl-bar" style="left:34px;top:140px;background:var(--orange)"></div>
  <div class="tl-box" style="left:50px;top:164px;border-color:var(--orange)">A record year with over 150 volunteers supporting the effort. 2014 will mark Lumarend Serves' 30th well.</div>

  <div class="tl-year" style="left:96px;top:114px">IN 2012</div>
  <div class="tl-bar" style="left:88px;top:128px;background:var(--green)"></div>
  <div class="tl-box" style="left:104px;top:150px;border-color:var(--green)">Lumarend Serves formed and $50,000 raised to bring on Stonehill M-60 drill rig and Halden H-250 Drilling Truck.</div>

  <div class="tl-year" style="left:150px;top:102px">IN 2010</div>
  <div class="tl-bar" style="left:142px;top:116px;background:var(--sky)"></div>
  <div class="tl-box" style="left:160px;top:140px;border-color:var(--sky)">First successful well, drilled in the Las Brisas neighborhood of Palmital. Its still providing clean water to this day.</div>

  <div class="tl-year" style="left:204px;top:90px">IN 2007</div>
  <div class="tl-bar" style="left:196px;top:104px;background:var(--red)"></div>
  <div class="tl-box" style="left:220px;top:124px;border-color:var(--red)">While on a mission trip to Las Brisas FHCCP is made aware of the many slums around Las Brisas without water.</div>

  <div class="tl-year" style="left:258px;top:78px">IN 1996</div>
  <div class="tl-bar" style="left:250px;top:92px;background:var(--green)"></div>
  <div class="tl-box" style="left:286px;top:112px;border-color:var(--green)">First Harbor Chapel of Cedar Point begins Mission trips to Northern Costa Rica.</div>

  <h2 class="abs heading our-team"><span class="gold">Our</span> <span class="blue">Team</span></h2>
  <div class="abs rule" style="left:176px;top:296px;width:80px"></div>
  <div class="abs rule" style="left:176px;top:300px;width:80px"></div>

  <div class="member" style="top:322px">
    <h3><svg width="14" height="8" viewBox="0 0 14 8"><path d="M0 1Q7 4 14 1M0 4Q7 7 14 4M0 7Q7 10 14 7" stroke="var(--blue)" stroke-width="1.4" fill="none"/></svg>FOUNDER AND PRESIDENT: MARTIN COLERIDGE</h3>
    <p>Sed ut perspiciatis unde omnis iste natus error sit voluptatem accusantium doloremque laudantium, totam rem aperiam, eaque ipsa quae ab illo inventore veritatis et quasi architecto beatae vitae dicta sunt explicabo. Nemo enim ipsam voluptatem quias saepe eveniet ut et voluptates repudiandae sint et molestiae</p>
  </div>
  <div class="portrait" style="top:318px"><span role="img" aria-label="Portrait of the founder and president" style="background:linear-gradient(#6b7f95,#2d3440)"></span></div>
  <div class="member-sep" style="top:394px"></div>

  <div class="member" style="top:408px">
    <h3><svg width="14" height="8" viewBox="0 0 14 8"><path d="M0 1Q7 4 14 1M0 4Q7 7 14 4M0 7Q7 10 14 7" stroke="var(--blue)" stroke-width="1.4" fill="none"/></svg>EXECUTIVE DIRECTOR: EVAN MARSH</h3>
    <p>Sed ut perspiciatis unde omnis iste natus error sit voluptatem accusantium doloremque laudantium, totam rem aperiam, eaque ipsa quae ab illo inventore veritatis et quasi architecto beatae vitae dicta sunt explicabo. Nemo enim ipsam voluptatem quias saepe eveniet ut et voluptates repudiandae sint et molestiae</p>
  </div>
  <div class="portrait" style="top:404px"><span role="img" aria-label="Portrait of the executive director" style="background:linear-gradient(#9a8a78,#7a3a34)"></span></div>
  <div class="member-sep" style="top:480px"></div>

  <div class="member" style="top:494px">
    <h3><svg width="14" height="8" viewBox="0 0 14 8"><path d="M0 1Q7 4 14 1M0 4Q7 7 14 4M0 7Q7 10 14 7" stroke="var(--blue)" stroke-width="1.4" fill="none"/></svg>FIELD MANAGER: TOMAS RUIZ</h3>
    <p>Sed ut perspiciatis unde omnis iste natus error sit voluptatem accusantium doloremque laudantium, totam rem aperiam, eaque ipsa quae ab illo inventore veritatis et quasi architecto beatae vitae dicta sunt explicabo. Nemo enim ipsam voluptatem quias saepe eveniet ut et voluptates repudiandae sint et molestiae</p>
  </div>
  <div class="portrait" style="top:490px"><span role="img" aria-label="Portrait of the field manager" style="background:linear-gradient(#8d8070,#d9772e)"></span></div>

  <div class="abs folio folio--right">www.lumarendserves.org<span class="num">3</span></div>
</section>

</body>
</html>
```